Presentation Folder and Insert

We need design for a standard 9 x 12 presentation folder.

We need design for one template for a 8.5 x 11 insert/sales sheet(s) that will go inside the presentation folder.

See attached layout for presentation folder.

Left and Right flap on inside with slits on right flap for business card.

Would like design and colour schemes for both folder and insert template to flow with look of attached business card.

Target Market(s)

small business owners, marketing managers, media buyers and advertising agencies.

Industry/Entity Type

Business

Requirements
Must have
• Bright and colourful on front, back and inside.

Template for insert should flow with look of folder.

Insert will need room for us to add our own content.

```html
<!DOCTYPE html>
<html lang="en">
<head>
<meta charset="utf-8">
<title>Vantora Media Network – Presentation Folder and Insert</title>
<link href="https://fonts.googleapis.com/css2?family=Open+Sans:wght@400;600;700&display=swap" rel="stylesheet">
<style>
  :root {
    --page-bg: #dfe4ea;
    --blue: #2566bb;
    --blue-deep: #174b92;
    --blue-panel: #1c5299;
    --white: #ffffff;
    --silver: #d6dadf;
    --silver-dark: #9aa3ad;
    --ink: #222831;
    --ink-soft: #4a525c;
    --faint: rgba(255, 255, 255, 0.32);
  }
  * { box-sizing: border-box; margin: 0; padding: 0; }
  html, body { width: 1200px; height: 960px; overflow: hidden; }
  body {
    background: var(--page-bg);
    font-family: "Open Sans", Arial, sans-serif;
    color: var(--ink);
    position: relative;
  }
  .piece { position: absolute; box-shadow: 0 6px 18px rgba(20, 40, 80, 0.18); }
  .piece > svg { position: absolute; inset: 0; display: block; }
  .layer { position: absolute; }

  /* Brand name setting */
  .brand {
    display: inline-flex; align-items: center; gap: 6px;
    font-weight: 700; letter-spacing: -0.5px; line-height: 1;
    color: var(--blue);
  }
  .brand-mark { display: inline-block; background: currentColor; }
  .brand--light { color: var(--white); }
  .brand--faint { color: var(--faint); }

  /* Outside spread: back + front */
  .folder-outside { left: 60px; top: 40px; width: 660px; height: 440px; }
  .front-brand { left: 460px; top: 200px; font-size: 36px; }
  .front-brand .brand-mark { width: 22px; height: 22px; }
  .front-web {
    left: 338px; top: 424px; font-size: 6.5px; font-weight: 600;
    color: var(--white); letter-spacing: 0.3px;
  }
  .back-brand { left: 105px; top: 308px; font-size: 16px; }
  .back-brand .brand-mark { width: 10px; height: 10px; }
  .back-contact {
    left: 62px; top: 340px; width: 156px; text-align: center;
    color: var(--white); font-size: 7px; line-height: 1.45; font-weight: 600;
  }
  .back-contact .web { margin-top: 8px; }

  /* Letterhead insert */
  .letterhead { left: 780px; top: 40px; width: 340px; height: 440px; background: var(--white); }
  .lh-brand { left: 20px; top: 22px; font-size: 20px; }
  .lh-brand .brand-mark { width: 12px; height: 12px; }
  .lh-body { left: 26px; top: 72px; width: 290px; font-size: 6px; line-height: 1.5; color: var(--ink-soft); }
  .lh-body .recipient { font-weight: 700; color: var(--ink); margin-bottom: 8px; font-size: 6.5px; }
  .lh-body p { margin-bottom: 8px; text-align: justify; }
  .lh-sign { left: 26px; top: 345px; width: 90px; }
  .lh-sign .rule { height: 1px; background: var(--silver-dark); margin-bottom: 4px; }
  .lh-sign .signer { font-size: 6px; font-weight: 700; }
  .lh-contact { left: 232px; top: 372px; font-size: 4.6px; line-height: 1.5; color: var(--ink-soft); }

  /* Inside spread */
  .folder-inside { left: 270px; top: 500px; width: 660px; height: 440px; }
  .insert-brand { left: 36px; top: 28px; font-size: 18px; }
  .insert-brand .brand-mark { width: 11px; height: 11px; }
  .insert-body { left: 40px; top: 72px; width: 262px; font-size: 5.6px; line-height: 1.5; color: var(--ink-soft); }
  .insert-body .recipient { font-weight: 700; color: var(--ink); margin-bottom: 7px; font-size: 6px; }
  .insert-body p { margin-bottom: 7px; text-align: justify; }
  .pockets { z-index: 2; }
  .pocket-brand { left: 16px; top: 396px; font-size: 15px; z-index: 3; }
  .pocket-brand .brand-mark { width: 9px; height: 9px; }
  .pocket-web { left: 16px; top: 418px; font-size: 5.5px; font-weight: 600; color: var(--ink); z-index: 3; }
  .inside-watermark { left: 420px; top: 86px; font-size: 38px; z-index: 1; }
  .inside-watermark .brand-mark { width: 22px; height: 22px; }

  /* Business card in slits */
  .card { left: 362px; top: 326px; width: 130px; height: 74px; z-index: 3; color: var(--white); }
  .card-name { position: absolute; left: 8px; top: 8px; font-size: 6.5px; font-weight: 700; }
  .card-details { position: absolute; left: 8px; top: 24px; font-size: 4.2px; line-height: 1.5; }
  .card-phone { position: absolute; left: 8px; top: 62px; font-size: 4.4px; font-weight: 600; }
  .card-brand-box {
    position: absolute; right: 8px; top: 20px; width: 44px; height: 32px;
    background: var(--white); border-radius: 3px;
    display: flex; align-items: center; justify-content: center;
  }
  .card-brand-box .brand { font-size: 9px; gap: 3px; }
  .card-brand-box .brand-mark { width: 5px; height: 5px; }
</style>
</head>
<body>

  <!-- Folder outside: back panel (left) and front cover (right) -->
  <section class="piece folder-outside" aria-label="Folder outside, back and front cover">
    <svg viewBox="0 0 660 440" width="660" height="440" aria-hidden="true">
      <defs>
        <linearGradient id="coverSilver" x1="0" y1="0" x2="1" y2="1">
          <stop offset="0" stop-color="#ffffff"/>
          <stop offset="0.6" stop-color="#f1f3f5"/>
          <stop offset="1" stop-color="#d6dadf"/>
        </linearGradient>
      </defs>
      <rect width="660" height="440" fill="var(--blue)"/>
      <line x1="330" y1="0" x2="330" y2="440" stroke="var(--blue-deep)" stroke-width="1.5"/>
      <path d="M546 0 C404 92 404 348 546 440 H660 V0 Z" fill="var(--silver-dark)"/>
      <path d="M560 0 C420 90 420 350 560 440 H660 V0 Z" fill="url(#coverSilver)"/>
      <rect x="62" y="298" width="156" height="124" rx="6" fill="var(--blue-panel)"/>
    </svg>
    <div class="layer brand front-brand"><span class="brand-mark"></span>Vantora</div>
    <div class="layer front-web">WWW.VANTORAMEDIA.EXAMPLE</div>
    <div class="layer brand brand--light back-brand"><span class="brand-mark"></span>Vantora</div>
    <address class="layer back-contact" style="font-style:normal">
      <div>Suite 410, 88 Harbour Road</div>
      <div>Riverton, BC V0A 1A0</div>
      <div style="margin-top:6px">Toll Free: 800-555-0142</div>
      <div class="web">www.vantoramedia.example</div>
    </address>
  </section>

  <!-- Letterhead / sales sheet insert -->
  <section class="piece letterhead" aria-label="Letterhead insert">
    <svg viewBox="0 0 340 440" width="340" height="440" aria-hidden="true">
      <path d="M110 0 H340 V44 C270 14 190 4 110 0 Z" fill="var(--blue)"/>
      <path d="M0 0 H110 C70 2 30 8 0 16 Z" fill="var(--silver)"/>
      <path d="M340 392 C310 414 270 432 236 440 H340 Z" fill="var(--blue)"/>
    </svg>
    <div class="layer brand lh-brand"><span class="brand-mark"></span>Vantora</div>
    <div class="layer lh-body">
      <div class="recipient">Dana Miller</div>
      <p>Vantora Media Network is a regional out-of-home media company placing indoor billboards and banners in busy venues such as restaurants, gyms, campuses and sports arenas.</p>
      <p>Our placements reach audiences where they relax and gather, giving local brands steady exposure at high traffic properties across the province.</p>
      <p>Vantora Media Network is a regional out-of-home media company placing indoor billboards and banners in busy venues such as restaurants, gyms, campuses and sports arenas.</p>
      <p>Our placements reach audiences where they relax and gather, giving local brands steady exposure at high traffic properties across the province.</p>
      <p>Vantora Media Network is a regional out-of-home media company placing indoor billboards and banners in busy venues such as restaurants, gyms, campuses and sports arenas.</p>
    </div>
    <div class="layer lh-sign">
      <div class="rule"></div>
      <div class="signer">Leo Hartwell</div>
    </div>
    <address class="layer lh-contact" style="font-style:normal">
      <div>Suite 410, 88 Harbour Road</div>
      <div>Riverton, BC V0A 1A0</div>
      <div>T 800-555-0142</div>
      <div>F 800-555-0143</div>
      <div>hello@vantoramedia.example</div>
      <div>www.vantoramedia.example</div>
    </address>
  </section>

  <!-- Folder inside: left pocket with insert, right pocket with card slits -->
  <section class="piece folder-inside" aria-label="Folder inside with pockets">
    <svg viewBox="0 0 660 440" width="660" height="440" aria-hidden="true">
      <rect width="660" height="440" fill="var(--blue)"/>
      <line x1="330" y1="0" x2="330" y2="440" stroke="var(--blue-deep)" stroke-width="1.5"/>
      <rect x="18" y="12" width="296" height="428" fill="var(--white)"/>
      <path d="M120 12 H314 V48 C250 22 185 14 120 12 Z" fill="var(--blue)"/>
    </svg>
    <div class="layer brand insert-brand"><span class="brand-mark"></span>Vantora</div>
    <div class="layer insert-body">
      <div class="recipient">Dana Miller</div>
      <p>Vantora Media Network is a regional out-of-home media company placing indoor billboards and banners in busy venues such as restaurants, gyms, campuses and sports arenas.</p>
      <p>Our placements reach audiences where they relax and gather, giving local brands steady exposure at high traffic properties across the province.</p>
      <p>Vantora Media Network is a regional out-of-home media company placing indoor billboards and banners in busy venues such as restaurants, gyms, campuses and sports arenas.</p>
      <p>Our placements reach audiences where they relax and gather, giving local brands steady exposure at high traffic properties across the province.</p>
    </div>
    <div class="layer brand brand--faint inside-watermark"><span class="brand-mark"></span>Vantora</div>

    <svg class="pockets" viewBox="0 0 660 440" width="660" height="440" aria-hidden="true">
      <defs>
        <linearGradient id="pocketSilver" x1="0" y1="0" x2="0" y2="1">
          <stop offset="0" stop-color="#ffffff"/>
          <stop offset="1" stop-color="#d9dde2"/>
        </linearGradient>
      </defs>
      <path d="M0 232 C120 236 236 196 330 150 V440 H0 Z" fill="url(#pocketSilver)"/>
      <path d="M0 232 C120 236 236 196 330 150" fill="none" stroke="var(--silver-dark)" stroke-width="1"/>
      <path d="M330 232 C450 236 566 196 660 150 V440 H330 Z" fill="url(#pocketSilver)"/>
      <path d="M330 232 C450 236 566 196 660 150" fill="none" stroke="var(--silver-dark)" stroke-width="1"/>
      <g stroke="var(--silver-dark)" stroke-width="1.2" fill="none">
        <path d="M356 334 L368 322"/>
        <path d="M486 322 L498 334"/>
        <path d="M356 392 L368 404"/>
        <path d="M486 404 L498 392"/>
      </g>
      <rect x="362" y="326" width="130" height="74" rx="3" fill="var(--blue)"/>
    </svg>
    <div class="layer brand pocket-brand"><span class="brand-mark"></span>Vantora</div>
    <div class="layer pocket-web">WWW.VANTORAMEDIA.EXAMPLE</div>

    <div class="layer card" aria-label="Business card">
      <div class="card-name">Leo Hartwell</div>
      <div class="card-details">
        <div>Account Director</div>
        <div>Suite 410, 88 Harbour Road</div>
        <div>Riverton, BC</div>
      </div>
      <div class="card-phone">Toll Free 800-555-0142</div>
      <div class="card-brand-box"><span class="brand"><span class="brand-mark"></span>Vantora</span></div>
    </div>
  </section>

</body>
</html>
```